Harwick Lending Hard Money Lender

We are looking for this flyer to be redesigned. We would like it to be even more simple than the attached design. No photos, no exclamation points, a 3-4 color palate maximum. We would do not want any graphics around the "Harwick Lending" logo.

```html
<!DOCTYPE html>
<html lang="en">
<head>
<meta charset="utf-8">
<title>Harwick Lending – Hard Money Loans</title>
<link rel="stylesheet" href="https://fonts.googleapis.com/css2?family=Alegreya+Sans:wght@400;500;700;800&family=Roboto:wght@300;700&display=swap">
<style>
  :root {
    --brand-blue: #0a4d8c;
    --ink-navy: #1b2a3a;
    --paper-white: #ffffff;
  }
  * { margin: 0; padding: 0; box-sizing: border-box; }
  html, body { width: 927px; height: 1200px; overflow: hidden; background: var(--ink-navy); }
  .flyer {
    position: relative;
    width: 927px;
    height: 1200px;
    background: var(--ink-navy);
    color: var(--paper-white);
    font-family: "Alegreya Sans", sans-serif;
    overflow: hidden;
  }
  .masthead {
    position: absolute; left: 0; top: 0;
    width: 927px; height: 204px;
    background: var(--brand-blue);
    display: flex; align-items: center; justify-content: center;
  }
  .brand-name {
    font-family: "Alegreya Sans", sans-serif;
    font-weight: 500;
    font-size: 62px;
    letter-spacing: 3px;
    color: var(--paper-white);
  }
  .headline {
    position: absolute; left: 0; top: 305px; width: 927px;
    text-align: center;
    font-weight: 800;
    font-size: 70px;
    letter-spacing: 1px;
  }
  .rate-line {
    position: absolute; left: 0; top: 406px; width: 927px;
    padding-left: 30px;
    text-align: center;
    font-family: "Roboto", sans-serif;
    font-weight: 700;
    font-size: 31px;
  }
  .loan-types {
    position: absolute; left: 128px; top: 488px;
    list-style: none;
    font-weight: 700;
    font-size: 34px;
  }
  .loan-types li { height: 73px; line-height: 48px; }
  .loan-types li::before { content: "\2022"; margin-right: 8px; }
  .benefits {
    position: absolute; left: 122px; top: 738px;
    list-style: none;
    font-weight: 700;
    font-size: 35px;
  }
  .benefits li { display: flex; align-items: center; height: 62px; }
  .benefits svg { width: 36px; height: 32px; margin-right: 14px; flex: none; }
  .benefits .note { font-weight: 400; }
  .contact-panel { position: absolute; left: 0; top: 0; width: 927px; height: 1200px; pointer-events: none; }
  .contact-item {
    position: absolute;
    font-family: "Roboto", sans-serif;
    font-weight: 300;
    color: var(--paper-white);
    display: flex; align-items: center;
  }
  .contact-item svg { flex: none; }
  .phone { left: 34px; top: 1018px; font-size: 37px; }
  .phone svg { width: 66px; height: 46px; margin-right: 22px; }
  .address { left: 34px; top: 1088px; font-size: 26px; line-height: 31px; }
  .address svg { width: 76px; height: 78px; margin-right: 18px; }
  .web { left: 504px; top: 1112px; font-size: 26px; }
  .email { left: 504px; top: 1152px; font-size: 26px; }
  .web svg, .email svg { width: 32px; height: 32px; margin-right: 18px; }
</style>
</head>
<body>
<main class="flyer">
  <header class="masthead">
    <span class="brand-name">HARWICK LENDING</span>
  </header>

  <h1 class="headline">Hard Money Loans</h1>
  <p class="rate-line">Rates From 8%</p>

  <ul class="loan-types">
    <li>Fix &amp; Flip Loans</li>
    <li>Commercial Loans</li>
    <li>Hard Money Loans</li>
  </ul>

  <ul class="benefits">
    <li><svg viewBox="0 0 36 32"><path d="M2 18 L8 13 L14 21 L31 2 L35 5 L14 30 Z" fill="var(--paper-white)"/></svg>Same–Day Approval</li>
    <li><svg viewBox="0 0 36 32"><path d="M2 18 L8 13 L14 21 L31 2 L35 5 L14 30 Z" fill="var(--paper-white)"/></svg>No Processing, Appraisal, or Extra Fees</li>
    <li><svg viewBox="0 0 36 32"><path d="M2 18 L8 13 L14 21 L31 2 L35 5 L14 30 Z" fill="var(--paper-white)"/></svg>100% Financing&nbsp;<span class="note">(w/ Additional Collateral)</span></li>
  </ul>

  <svg class="contact-panel" viewBox="0 0 927 1200" aria-hidden="true">
    <polygon points="0,990 354,990 464,1200 0,1200" fill="var(--brand-blue)"/>
    <polygon points="424,1104 927,1104 927,1200 476,1200" fill="var(--brand-blue)"/>
  </svg>

  <div class="contact-item phone">
    <svg viewBox="0 0 66 46"><path d="M4 16 C4 4 62 4 62 16 L62 20 L48 20 L48 13 C40 10 26 10 18 13 L18 20 L4 20 Z" fill="var(--paper-white)"/><path d="M16 22 L50 22 L58 44 L8 44 Z" fill="var(--paper-white)"/><circle cx="33" cy="33" r="8" fill="var(--brand-blue)"/><circle cx="33" cy="33" r="4" fill="var(--paper-white)"/></svg>
    303.555.0142
  </div>

  <div class="contact-item address">
    <svg viewBox="0 0 76 78"><path d="M38 4 C24 4 15 14 15 26 C15 40 38 60 38 60 C38 60 61 40 61 26 C61 14 52 4 38 4 Z" fill="var(--paper-white)"/><circle cx="38" cy="26" r="9" fill="var(--brand-blue)"/><ellipse cx="38" cy="64" rx="34" ry="11" fill="none" stroke="var(--paper-white)" stroke-width="5"/><ellipse cx="38" cy="64" rx="14" ry="4" fill="var(--paper-white)"/></svg>
    <span>4810 Alder Ridge Blvd<br>Suite 210 Denver<br>CO 80239</span>
  </div>

  <div class="contact-item web">
    <svg viewBox="0 0 32 32"><circle cx="16" cy="16" r="14" fill="var(--paper-white)"/><g fill="none" stroke="var(--brand-blue)" stroke-width="2"><circle cx="16" cy="16" r="10"/><ellipse cx="16" cy="16" rx="4.5" ry="10"/><line x1="6" y1="16" x2="26" y2="16"/><line x1="8" y1="11" x2="24" y2="11"/><line x1="8" y1="21" x2="24" y2="21"/></g></svg>
    www.harwicklending.com
  </div>

  <div class="contact-item email">
    <svg viewBox="0 0 32 32"><circle cx="16" cy="16" r="15" fill="var(--paper-white)"/><rect x="8" y="10" width="16" height="12" fill="var(--brand-blue)"/><path d="M8 10 L16 17 L24 10 M8 22 L14 16 M24 22 L18 16" fill="none" stroke="var(--paper-white)" stroke-width="1.5"/></svg>
    loans@harwicklending.com
  </div>
</main>
</body>
</html>
```